PowerPoint Template Design

We are an independent private equity and advisory firm (mergers and acquisitions), based in Brazil. We are looking for a power point template to use for companies presentations to investors and other targets (ie competitors).
Find attached the actual template that we use, we need something with this structure but more customized.

- Cover slide with our logo, project name and current date
- Index/Agenda slide
- Content slides
a. Slide with title, subtitle, text and footer. The footer should contain the page number, the person who we are sending to and the word "CONFIDENTIAL"
b. Slide with title, subtitle, text and pictures/charters/graphics
- Final slide with adress and contacts

We do not want something very colorful, we need something plain, simple but modern.

Target Market(s)

Investors, CEOs, CFOs, other advisory firms like DNTallis, DSRH, Almsbury, etc.

Industry/Entity Type

Equity

Requirements
Must have
• - the same colors used by our designer;
- one font only (Century Gothic);

```html
<!DOCTYPE html>
<html lang="en">
<head>
<meta charset="utf-8">
<title>Tessaly – Presentation Template</title>
<link rel="stylesheet" href="https://fonts.googleapis.com/css2?family=Questrial&display=swap">
<style>
:root{
  --stage:#8a8a8a;
  --paper:#fbfbfb;
  --ink:#2b2b2b;
  --muted:#555;
  --charcoal:#545454;
  --footer:#2a2a2a;
  --gold:#f5b800;
  --gold-soft:#fcd12a;
  --row-a:#fcd34d;
  --row-b:#fde9a6;
  --olive:#c8ad55;
  --orange:#f7941d;
}
*{box-sizing:border-box;margin:0;padding:0}
html,body{width:1200px;height:911px;overflow:hidden;background:var(--stage);font-family:"Questrial",sans-serif;color:var(--ink)}
.slide{position:absolute;width:572px;height:428px;background:var(--paper);overflow:hidden}
.s1{left:18px;top:15px}.s2{left:605px;top:15px}.s3{left:18px;top:463px}.s4{left:605px;top:463px}

.brand{position:absolute;left:11px;top:14px;width:50px;display:flex;flex-direction:column;align-items:center;gap:6px}
.brand .mark{width:14px;height:14px;background:var(--gold)}
.brand .name{font-size:11px;color:var(--ink)}
.title{position:absolute;left:70px;top:10px;font-size:23px;font-weight:400;color:var(--ink)}
.rule{position:absolute;left:70px;top:40px;width:396px;height:1px;background:var(--gold)}
.subtitle{position:absolute;left:70px;top:45px;font-size:12px;color:var(--muted)}

.footer{position:absolute;left:0;bottom:0;width:100%;height:26px;background:var(--footer);border-top:4px solid var(--gold);font-size:10.5px;color:var(--gold)}
.footer .to{position:absolute;left:54px;top:6px}
.footer .conf{position:absolute;right:38px;top:6px}
.pager{position:absolute;left:232px;top:4px;display:flex;align-items:center;gap:8px}
.pager .num{background:var(--gold);color:var(--footer);border-radius:2px;padding:0 6px;font-size:10px;line-height:13px}
.pager .sep{color:var(--gold);font-size:13px}
.pager svg{display:block}

.tag{position:absolute;background:var(--charcoal);color:var(--gold);font-size:12.5px;display:flex;align-items:center;justify-content:center;text-align:center;box-shadow:3px 3px 5px rgba(0,0,0,.25)}
.body{position:absolute;font-size:12px;line-height:19px;color:var(--ink)}
.body p+p{margin-top:19px}
.divider{position:absolute;left:284px;top:119px;height:271px;border-left:1px dashed #bbb}

.card{width:100px;height:90px;line-height:17px}
.card-text{position:absolute;top:218px;width:104px;font-size:10px;line-height:11.5px}

.data{position:absolute;left:61px;top:86px;width:457px;border-collapse:collapse;font-size:7px;text-align:center;box-shadow:0 6px 6px -4px rgba(0,0,0,.3)}
.data th{background:var(--charcoal);color:#fff;height:32px;font-size:10px;letter-spacing:1px;font-weight:400;border-left:1px solid #777;line-height:13px}
.data th:first-child{border-left:0}
.data td{height:18.3px;letter-spacing:1px}
.data td:first-child{font-size:11px}
.data tr:nth-child(odd) td{background:var(--row-a)}
.data tr:nth-child(even) td{background:var(--row-b)}
.inference{left:6px;top:296px;width:100px;height:18px;font-size:12.5px;letter-spacing:.5px}
.note{position:absolute;left:67px;top:338px;width:447px;font-size:12px;line-height:13.5px;text-align:justify;text-indent:58px;color:var(--ink)}
.chart{position:absolute;left:0;top:0}
</style>
</head>
<body>

<section class="slide s1">
  <div class="brand"><span class="mark"></span><span class="name">Tessaly</span></div>
  <h1 class="title">Slide Title Goes Here</h1><div class="rule"></div>
  <p class="subtitle">Subtitle of the slide goes here or any tagline goes here</p>
  <div class="tag" style="left:32px;top:85px;width:212px;height:26px">HEADING ONE GOES HERE</div>
  <div class="tag" style="left:320px;top:85px;width:212px;height:26px">HEADING TWO GOES HERE</div>
  <div class="divider"></div>
  <div class="body" style="left:38px;top:140px;width:212px">
    <p>• Lorem ipsum dolor sit amet, consectetur adipiscing elit. Suspendisse iaculis tempor metus</p>
    <p>• Vivamus eu enim eu nibh ornare tincidunt vitae a dui. Nulla facilisi. Praesent tempus, sem non pellentesque tristique,</p>
    <p>• Cum sociis natoque penatibus et magnis dis parturient montes, nascetur ridiculus mus. Nam nec libero sed dui lobortis bibendum</p>
  </div>
  <div class="body" style="left:330px;top:140px;width:212px">
    <p>• Lorem ipsum dolor sit amet, consectetur adipiscing elit. Suspendisse iaculis tempor metus</p>
    <p>• Vivamus eu enim eu nibh ornare tincidunt vitae a dui. Nulla facilisi. Praesent tempus, sem non pellentesque tristique,</p>
    <p>• Cum sociis natoque penatibus et magnis dis parturient montes, nascetur ridiculus mus. Nam nec libero sed dui lobortis bibendum</p>
  </div>
  <footer class="footer"><span class="to">Addressee Name</span>
    <div class="pager"><svg width="7" height="10"><path d="M6 0L0 5l6 5z" fill="var(--gold)"/></svg><span class="num">01</span><span class="sep">/</span><span class="num">10</span><svg width="7" height="10"><path d="M1 0l6 5-6 5z" fill="var(--gold)"/></svg></div>
    <span class="conf">Confidential 2013</span></footer>
</section>

<section class="slide s2">
  <div class="brand"><span class="mark"></span><span class="name">Tessaly</span></div>
  <h1 class="title">Slide Title Goes Here</h1><div class="rule"></div>
  <p class="subtitle">Subtitle of the slide goes here or any tagline goes here</p>
  <div class="tag card" style="left:33px;top:94px">HEADING ONE<br>GOES HERE</div>
  <div class="tag card" style="left:159px;top:94px">HEADING TWO<br>GOES HERE</div>
  <div class="tag card" style="left:285px;top:94px">HEADING<br>THREE GOES<br>HERE</div>
  <div class="tag card" style="left:416px;top:94px">HEADING<br>FOUR GOES<br>HERE</div>
  <p class="card-text" style="left:35px">Lorem ipsum dolor sit amet, consectetur adipiscing elit. Suspendisse iaculis tempor metus Vivamus eu enim eu nibh ornare tincidunt vitae a dui. Nulla facilisi. Praesent tempus, sem non pellentesque tristique,</p>
  <p class="card-text" style="left:160px">Lorem ipsum dolor sit amet, consectetur adipiscing elit. Suspendisse iaculis tempor metus Vivamus eu enim eu nibh ornare tincidunt vitae a dui. Nulla facilisi. Praesent tempus, sem non pellentesque tristique,</p>
  <p class="card-text" style="left:290px">Lorem ipsum dolor sit amet, consectetur adipiscing elit. Suspendisse iaculis tempor metus Vivamus eu enim eu nibh ornare tincidunt vitae a dui. Nulla facilisi. Praesent tempus, sem non pellentesque tristique,</p>
  <p class="card-text" style="left:420px">Lorem ipsum dolor sit amet, consectetur adipiscing elit. Suspendisse iaculis tempor metus Vivamus eu enim eu nibh ornare tincidunt vitae a dui. Nulla facilisi. Praesent tempus, sem non pellentesque tristique,</p>
  <footer class="footer"><span class="to">Addressee Name</span>
    <div class="pager"><svg width="7" height="10"><path d="M6 0L0 5l6 5z" fill="var(--gold)"/></svg><span class="num">01</span><span class="sep">/</span><span class="num">10</span><svg width="7" height="10"><path d="M1 0l6 5-6 5z" fill="var(--gold)"/></svg></div>
    <span class="conf">Confidential 2013</span></footer>
</section>

<section class="slide s3">
  <div class="brand"><span class="mark"></span><span class="name">Tessaly</span></div>
  <h1 class="title">Slide Title Goes Here</h1><div class="rule"></div>
  <p class="subtitle">Subtitle of the slide goes here or any tagline goes here</p>
  <table class="data">
    <thead><tr><th>BRANDS /<br>MONTH</th><th>JAN</th><th>FEB</th><th>MAR</th><th>APR</th></tr></thead>
    <tbody>
      <tr><td>A</td><td>5</td><td>7</td><td>9</td><td>11</td></tr>
      <tr><td>B</td><td>10</td><td>12</td><td>14</td><td>16</td></tr>
      <tr><td>C</td><td>15</td><td>17</td><td>19</td><td>21</td></tr>
      <tr><td>D</td><td>20</td><td>22</td><td>24</td><td>26</td></tr>
      <tr><td>E</td><td>25</td><td>27</td><td>29</td><td>31</td></tr>
      <tr><td>F</td><td>30</td><td>32</td><td>34</td><td>36</td></tr>
      <tr><td>G</td><td>35</td><td>37</td><td>39</td><td>41</td></tr>
      <tr><td>H</td><td>40</td><td>42</td><td>44</td><td>46</td></tr>
    </tbody>
  </table>
  <div class="tag inference">INFERENCE</div>
  <p class="note">Vivamus eu enim eu nibh ornare tincidunt vitae a dui. Nulla facilisi. Praesent tempus, sem non pellentesque tristique, arcu sapien sollicitudin justo, vel pellentesque sapien ipsum at lectus</p>
  <footer class="footer"><span class="to">Addressee Name</span>
    <div class="pager"><svg width="7" height="10"><path d="M6 0L0 5l6 5z" fill="var(--gold)"/></svg><span class="num">01</span><span class="sep">/</span><span class="num">10</span><svg width="7" height="10"><path d="M1 0l6 5-6 5z" fill="var(--gold)"/></svg></div>
    <span class="conf">Confidential 2013</span></footer>
</section>

<section class="slide s4">
  <div class="brand"><span class="mark"></span><span class="name">Tessaly</span></div>
  <h1 class="title">Slide Title Goes Here</h1><div class="rule"></div>
  <p class="subtitle">Subtitle of the slide goes here or any tagline goes here</p>
  <svg class="chart" width="572" height="290" viewBox="0 0 572 290" font-family="Questrial, sans-serif" font-size="10" fill="#555">
    <g stroke="var(--gold-soft)" stroke-width="1">
      <line x1="85" y1="99" x2="479" y2="99"/><line x1="85" y1="125" x2="479" y2="125"/>
      <line x1="85" y1="151" x2="479" y2="151"/><line x1="85" y1="177" x2="479" y2="177"/>
      <line x1="85" y1="202" x2="479" y2="202"/><line x1="85" y1="228" x2="479" y2="228"/>
      <line x1="479" y1="99" x2="479" y2="254"/>
      <line x1="85" y1="99" x2="85" y2="254"/><line x1="85" y1="254" x2="479" y2="254"/>
    </g>
    <g text-anchor="end">
      <text x="76" y="103">6</text><text x="76" y="129">5</text><text x="76" y="155">4</text>
      <text x="76" y="181">3</text><text x="76" y="206">2</text><text x="76" y="232">1</text><text x="76" y="258">0</text>
    </g>
    <g text-anchor="middle"><text x="136" y="270">A</text><text x="234" y="270">B</text><text x="333" y="270">C</text><text x="431" y="270">D</text></g>
    <g>
      <rect x="104" y="143" width="21" height="111" fill="var(--olive)"/><rect x="125" y="192" width="21" height="62" fill="var(--orange)"/><rect x="146" y="202" width="21" height="52" fill="var(--gold-soft)"/>
      <rect x="201" y="125" width="21" height="129" fill="var(--olive)"/><rect x="222" y="140" width="21" height="114" fill="var(--orange)"/><rect x="243" y="202" width="21" height="52" fill="var(--gold-soft)"/>
      <rect x="300" y="151" width="21" height="103" fill="var(--olive)"/><rect x="321" y="207" width="21" height="47" fill="var(--orange)"/><rect x="342" y="215" width="21" height="39" fill="var(--gold-soft)"/>
      <rect x="399" y="112" width="21" height="142" fill="var(--olive)"/><rect x="420" y="182" width="21" height="72" fill="var(--orange)"/><rect x="441" y="184" width="21" height="70" fill="var(--gold-soft)"/>
    </g>
  </svg>
  <div class="tag inference">INFERENCE</div>
  <p class="note">Vivamus eu enim eu nibh ornare tincidunt vitae a dui. Nulla facilisi. Praesent tempus, sem non pellentesque tristique, arcu sapien sollicitudin justo, vel pellentesque sapien ipsum at lectus</p>
  <footer class="footer"><span class="to">Addressee Name</span>
    <div class="pager"><svg width="7" height="10"><path d="M6 0L0 5l6 5z" fill="var(--gold)"/></svg><span class="num">01</span><span class="sep">/</span><span class="num">10</span><svg width="7" height="10"><path d="M1 0l6 5-6 5z" fill="var(--gold)"/></svg></div>
    <span class="conf">Confidential 2013</span></footer>
</section>

</body>
</html>
```